Create a professional, eye-catching business card design that reflects the values and services of Brookfern Veterinary Hospital. we provide veterinary services and the business card should be a memorable representation of the clinic and align with its branding and mission. our tag line is "Life Long Companions, Lifelong Care"
Use clean, modern typography. Prioritize readability and professionalism. We would like to see designs that use the color blue, as in the logo example. the final design should communicate professionalism and care, with attention to detail.

```html
<!DOCTYPE html>
<html lang="en">
<head>
<meta charset="utf-8">
<title>Brookfern Veterinary Hospital – Business Card</title>
<link href="https://fonts.googleapis.com/css2?family=Lato:wght@400;700&family=Montserrat:ital,wght@0,800;1,700&display=swap" rel="stylesheet">
<style>
  :root{
    --navy:#1b3a78;
    --navy-deep:#13295a;
    --card-blue:#1c4585;
    --gold:#f3c613;
    --white:#ffffff;
    --ink-soft:#e7ecf6;
    --stage:#2b2b2b;
  }
  *{box-sizing:border-box;margin:0;padding:0}
  html,body{width:1200px;height:875px;overflow:hidden}
  body{background:var(--stage);font-family:"Lato",sans-serif;position:relative}

  .card{
    position:absolute;top:283px;width:540px;height:309px;border-radius:18px;overflow:hidden;
  }
  /* Back side */
  .card--services{left:40px;background:var(--card-blue);color:var(--white);padding:38px 34px}
  .card--services .accent-ring{
    position:absolute;right:-70px;top:-40px;width:300px;height:300px;border-radius:50%;
    border:2px solid rgba(255,255,255,.06);
  }
  .services-title{font-family:"Montserrat",sans-serif;font-weight:800;font-size:34px;letter-spacing:.5px;line-height:1}
  .services-subtitle{font-size:13px;margin-top:8px;color:var(--ink-soft)}
  .services-intro{font-size:12.5px;margin-top:6px;color:var(--gold)}
  .services-list{list-style:none;margin-top:8px}
  .services-list li{display:flex;align-items:center;gap:10px;font-size:15px;line-height:1.55}
  .services-list svg{flex:none;width:13px;height:13px;fill:var(--gold)}

  /* Front side */
  .card--contact{left:620px;background:var(--white);color:var(--navy)}
  .brand{
    position:absolute;left:34px;top:96px;width:210px;display:flex;flex-direction:column;align-items:center;gap:14px;text-align:center
  }
  .brand-mark{width:54px;height:54px;border-radius:50%;background:var(--navy)}
  .brand-name{font-family:"Montserrat",sans-serif;font-weight:800;font-size:21px;line-height:1.15;color:var(--navy);text-transform:uppercase}
  .divider{position:absolute;left:262px;top:60px;width:1.5px;height:150px;background:var(--navy)}
  .person{position:absolute;left:286px;top:58px}
  .person-name{font-family:"Montserrat",sans-serif;font-weight:800;font-size:24px;color:var(--navy);text-transform:uppercase;letter-spacing:.3px}
  .person-role{font-size:15px;color:var(--gold);margin-top:2px}
  .contact-list{list-style:none;margin-top:12px}
  .contact-list li{display:flex;align-items:flex-start;gap:10px;font-size:13.5px;line-height:1.45;color:var(--navy-deep)}
  .contact-list svg{flex:none;width:13px;height:13px;margin-top:3px;fill:var(--navy)}
  .tagline{
    position:absolute;left:0;right:0;bottom:30px;text-align:center;
    font-family:"Montserrat",sans-serif;font-style:italic;font-weight:700;font-size:19px;color:var(--navy)
  }
</style>
</head>
<body>

<section class="card card--services" aria-label="Services side">
  <div class="accent-ring" aria-hidden="true"></div>
  <h2 class="services-title">OUR SERVICES</h2>
  <p class="services-subtitle">Personalised &amp; Compassionate Care for Your Companions</p>
  <p class="services-intro">We offer a full range of veterinary services to meet the health needs of your pets, including</p>
  <ul class="services-list">
    <li><svg viewBox="0 0 20 20"><circle cx="10" cy="13" r="5"/><circle cx="3" cy="7" r="2.3"/><circle cx="8" cy="3.5" r="2.3"/><circle cx="13" cy="3.5" r="2.3"/><circle cx="17.5" cy="7" r="2.3"/></svg>Preventive care (vaccinations, wellness exams, parasite control)</li>
    <li><svg viewBox="0 0 20 20"><circle cx="10" cy="13" r="5"/><circle cx="3" cy="7" r="2.3"/><circle cx="8" cy="3.5" r="2.3"/><circle cx="13" cy="3.5" r="2.3"/><circle cx="17.5" cy="7" r="2.3"/></svg>Diagnostic services (blood tests, x-rays, and more)</li>
    <li><svg viewBox="0 0 20 20"><circle cx="10" cy="13" r="5"/><circle cx="3" cy="7" r="2.3"/><circle cx="8" cy="3.5" r="2.3"/><circle cx="13" cy="3.5" r="2.3"/><circle cx="17.5" cy="7" r="2.3"/></svg>Surgery (routine and advanced procedures)</li>
    <li><svg viewBox="0 0 20 20"><circle cx="10" cy="13" r="5"/><circle cx="3" cy="7" r="2.3"/><circle cx="8" cy="3.5" r="2.3"/><circle cx="13" cy="3.5" r="2.3"/><circle cx="17.5" cy="7" r="2.3"/></svg>Emergency care</li>
    <li><svg viewBox="0 0 20 20"><circle cx="10" cy="13" r="5"/><circle cx="3" cy="7" r="2.3"/><circle cx="8" cy="3.5" r="2.3"/><circle cx="13" cy="3.5" r="2.3"/><circle cx="17.5" cy="7" r="2.3"/></svg>Dental care</li>
    <li><svg viewBox="0 0 20 20"><circle cx="10" cy="13" r="5"/><circle cx="3" cy="7" r="2.3"/><circle cx="8" cy="3.5" r="2.3"/><circle cx="13" cy="3.5" r="2.3"/><circle cx="17.5" cy="7" r="2.3"/></svg>Senior pet care and wellness programs</li>
  </ul>
</section>

<section class="card card--contact" aria-label="Contact side">
  <div class="brand">
    <span class="brand-mark" aria-hidden="true"></span>
    <span class="brand-name">Brookfern Veterinary Hospital</span>
  </div>
  <div class="divider" aria-hidden="true"></div>
  <div class="person">
    <h1 class="person-name">Daniel Harper</h1>
    <p class="person-role">Founder &amp; CEO</p>
    <ul class="contact-list">
      <li><svg viewBox="0 0 20 20"><path d="M10 1a6.5 6.5 0 0 0-6.5 6.5C3.5 12.5 10 19 10 19s6.5-6.5 6.5-11.5A6.5 6.5 0 0 0 10 1zm0 9a2.5 2.5 0 1 1 0-5 2.5 2.5 0 0 1 0 5z"/></svg><span>Your Address, City<br>State, Zip Code 1235</span></li>
      <li><svg viewBox="0 0 20 20"><path d="M4 1.5l3.5 0 1.5 4.5-2.2 1.6a11 11 0 0 0 5.6 5.6L14 11l4.5 1.5V16a2.5 2.5 0 0 1-2.5 2.5C8.3 18.5 1.5 11.7 1.5 4A2.5 2.5 0 0 1 4 1.5z"/></svg><span>(12) 5550 1843</span></li>
      <li><svg viewBox="0 0 20 20"><path d="M1.5 4h17v12h-17zM2.5 5l7.5 6 7.5-6" /><path d="M2 4.5l8 6.2 8-6.2v-.5H2z" fill="#fff"/></svg><span>office@brookfernvet.com.au</span></li>
      <li><svg viewBox="0 0 20 20"><path d="M10 1a9 9 0 1 0 0 18 9 9 0 0 0 0-18zm0 2c1.4 1.6 2.2 3.8 2.4 6H7.6C7.8 6.8 8.6 4.6 10 3zm-2.4 8h4.8c-.2 2.2-1 4.4-2.4 6-1.4-1.6-2.2-3.8-2.4-6zM3.1 9a7 7 0 0 1 3.8-5.3A11 11 0 0 0 5.6 9zm0 2h2.5a11 11 0 0 0 1.3 5.3A7 7 0 0 1 3.1 11zm11.3 0h2.5a7 7 0 0 1-3.8 5.3 11 11 0 0 0 1.3-5.3zm0-2a11 11 0 0 0-1.3-5.3A7 7 0 0 1 16.9 9z"/></svg><span>brookfernvet.com.au</span></li>
    </ul>
  </div>
  <p class="tagline">Lifelong Companions, Lifelong Care</p>
</section>

</body>
</html>
```